Hi,
We are an accounting firm looking to upgrade the following:
Logo, letterhead, withcomp slips and maybe our business cards. I have attached our original letterhead (sample A) and a letterhead (SAmple B) which we like the design and layout, however I want to stick with the colours of our orginal letterhead (Sample A) but improve and modernise the look with other letter head (Sample B) I have attached both. On the footer of Sample A, we would like to remove the names of the directors but leave EST. 1985 we also want to add the QRT logo ABN and TAX AGENT logo as stated in Sample B , we would like to do a layout for the header similar to SAmple B however maybe a bit more structured.

```html
<!DOCTYPE html>
<html lang="en">
<head>
<meta charset="utf-8">
<title>Brentholm Accountants – Stationery</title>
<link href="https://fonts.googleapis.com/css2?family=Montserrat:wght@400;500;600&display=swap" rel="stylesheet">
<style>
:root{
  --backdrop:#87888a;
  --paper:#ffffff;
  --brand-blue:#3d84c4;
  --brand-navy:#1b3e78;
  --brand-navy-deep:#102c5c;
  --ink:#1c1c1c;
  --black:#1a1a1a;
}
*{margin:0;padding:0;box-sizing:border-box}
html,body{width:1200px;height:1200px;overflow:hidden}
body{background:var(--backdrop);font-family:"Montserrat",Arial,sans-serif;color:var(--ink);position:relative}
.sprites{position:absolute;width:0;height:0}
.sheet{position:absolute;background:var(--paper);overflow:hidden}
.sheet-art{position:absolute;inset:0;width:100%;height:100%}
.letterhead{left:75px;top:72px;width:744px;height:1052px}
.card-front{left:601px;top:244px;width:500px;height:286px}
.card-back{left:601px;top:600px;width:500px;height:286px}

.wordmark{position:absolute;display:flex;align-items:center;gap:12px;color:var(--paper);font-weight:600;letter-spacing:-0.5px;line-height:1}
.wordmark-square{background:var(--paper);flex:none}
.letterhead .wordmark{left:40px;top:48px;font-size:50px}
.letterhead .wordmark-square{width:18px;height:18px}
.card-front .wordmark{left:30px;top:44px;font-size:33px;gap:8px}
.card-front .wordmark-square{width:12px;height:12px}
.card-back .wordmark{left:232px;top:182px;font-size:38px;gap:10px}
.card-back .wordmark-square{width:14px;height:14px}

.contact-list{position:absolute;list-style:none;text-align:right}
.contact-list li{display:flex;justify-content:flex-end;align-items:center;gap:9px;white-space:nowrap}
.contact-list svg{fill:var(--ink);flex:none}
.letterhead .contact-list{right:38px;top:38px;font-size:15px}
.letterhead .contact-list li{height:25.5px}
.letterhead .contact-list svg{width:13px;height:13px}
.card-front .contact-list{right:26px;top:179px;font-size:11.5px}
.card-front .contact-list li{height:20px;gap:7px}
.card-front .contact-list svg{width:10px;height:10px}

.legal{position:absolute;left:40px;top:928px;font-size:17.5px;line-height:1.3}
.legal .est{margin-top:6px}
.legal .firm-type{font-size:14.5px}
.address{position:absolute;right:40px;top:928px;text-align:right;font-size:17.5px;line-height:1.27;font-style:normal}
.address .company{font-weight:500;margin-bottom:4px}
.address .street{display:flex;justify-content:flex-end;align-items:center;gap:8px}
.address svg{width:12px;height:14px;fill:var(--ink)}

.card-meta{position:absolute;right:27px;top:37px;text-align:right;font-size:10.5px;line-height:1.3}
.card-abn{position:absolute;right:27px;top:106px;font-size:11px}
.card-company{position:absolute;left:29px;top:185px;font-size:13px;font-weight:500}
.card-address{position:absolute;left:29px;top:208px;font-size:10.5px;line-height:1.32;display:flex;gap:6px;font-style:normal}
.card-address svg{width:8px;height:11px;fill:var(--ink);margin-top:2px;flex:none}
</style>
</head>
<body>

<svg class="sprites" aria-hidden="true">
  <defs>
    <linearGradient id="navy-fade" x1="0" y1="0" x2="1" y2="0">
      <stop offset="0" stop-color="var(--brand-navy-deep)"/>
      <stop offset="1" stop-color="var(--brand-navy)"/>
    </linearGradient>
    <symbol id="icon-phone" viewBox="0 0 24 24"><path d="M6.6 10.8a15.1 15.1 0 0 0 6.6 6.6l2.2-2.2a1 1 0 0 1 1-.25 11.4 11.4 0 0 0 3.6.57 1 1 0 0 1 1 1V20a1 1 0 0 1-1 1A17 17 0 0 1 3 4a1 1 0 0 1 1-1h3.5a1 1 0 0 1 1 1c0 1.25.2 2.45.57 3.570a1 1 0 0 1-.25 1z"/></symbol>
    <symbol id="icon-fax" viewBox="0 0 24 24"><path d="M6 2h12v6H6zM3 9h18a1 1 0 0 1 1 1v8h-4v4H6v-4H2v-8a1 1 0 0 1 1-1zm5 8v3h8v-3z"/></symbol>
    <symbol id="icon-mail" viewBox="0 0 24 24"><path d="M2 5h20v14H2zm2 2v.5l8 5 8-5V7l-8 5z"/></symbol>
    <symbol id="icon-web" viewBox="0 0 24 24"><path d="M12 2a10 10 0 1 0 0 20 10 10 0 0 0 0-20zm-1 17.9A8 8 0 0 1 4.2 10.6L9 15.4v1a2 2 0 0 0 2 2zm6.9-2.5A2 2 0 0 0 16 16h-1v-3a1 1 0 0 0-1-1H8v-2h2a1 1 0 0 0 1-1V7h2a2 2 0 0 0 2-2v-.4a8 8 0 0 1 2.9 12.8z"/></symbol>
    <symbol id="icon-pin" viewBox="0 0 16 22"><path d="M8 0a8 8 0 0 0-8 8c0 6 8 14 8 14s8-8 8-14a8 8 0 0 0-8-8zm0 11a3 3 0 1 1 0-6 3 3 0 0 1 0 6z"/></symbol>
  </defs>
</svg>

<!-- Letterhead -->
<section class="sheet letterhead">
  <svg class="sheet-art" viewBox="0 0 744 1052" preserveAspectRatio="none" aria-hidden="true">
    <path d="M0 0H412C352 102 188 170 0 160Z" fill="var(--brand-blue)"/>
    <path d="M412 0H500C425 115 225 180 0 168V160C188 170 352 102 412 0Z" fill="url(#navy-fade)"/>
    <path d="M225 1052C290 975 460 888 744 888V891C480 890 320 975 256 1052Z" fill="var(--brand-blue)"/>
    <path d="M256 1052C320 975 480 890 744 891V894C520 898 400 960 350 1052Z" fill="var(--brand-navy)"/>
    <path d="M350 1052C400 960 520 898 744 894V896C530 900 430 940 375 1052Z" fill="var(--black)"/>
  </svg>
  <div class="wordmark"><span class="wordmark-square"></span>Brentholm</div>
  <ul class="contact-list">
    <li>+61 3 9400 2715<svg><use href="#icon-phone"/></svg></li>
    <li>+61 3 9400 2788<svg><use href="#icon-fax"/></svg></li>
    <li>info@brentholm.com.au<svg><use href="#icon-mail"/></svg></li>
    <li>www.brentholmaccountants.com.au<svg><use href="#icon-web"/></svg></li>
  </ul>
  <div class="legal">
    <p>ABN 41 602 915 378</p>
    <p class="est">EST. 1985</p>
    <p class="firm-type">Qualified Registered Accountants</p>
  </div>
  <address class="address">
    <p class="company">BRENTHOLM PTY LTD</p>
    <p class="street">27 Ashby Road<svg><use href="#icon-pin"/></svg></p>
    <p>Kewley, Vic. 3199</p>
    <p>Australia</p>
  </address>
</section>

<!-- Business card front -->
<section class="sheet card-front">
  <svg class="sheet-art" viewBox="0 0 400 229" preserveAspectRatio="none" aria-hidden="true">
    <path d="M0 0H262C215 78 118 114 0 108Z" fill="var(--brand-blue)"/>
    <path d="M262 0H325C250 95 130 122 0 115V108C118 114 215 78 262 0Z" fill="url(#navy-fade)"/>
    <path d="M90 229C122 188 200 163 282 167C212 176 152 200 126 229Z" fill="var(--brand-navy)"/>
  </svg>
  <div class="wordmark"><span class="wordmark-square"></span>Brentholm</div>
  <div class="card-meta">
    <p>EST. 1985</p>
    <p>Qualified Registered</p>
    <p>Accountants</p>
  </div>
  <p class="card-abn">ABN 41 602 915 378</p>
  <p class="card-company">BRENTHOLM PTY LTD</p>
  <address class="card-address">
    <svg><use href="#icon-pin"/></svg>
    <div><p>27 Ashby Road</p><p>Kewley, Vic. 3199</p><p>Australia</p></div>
  </address>
  <ul class="contact-list">
    <li>+61 3 9400 2715<svg><use href="#icon-phone"/></svg></li>
    <li>+61 3 9400 2788<svg><use href="#icon-fax"/></svg></li>
    <li>info@brentholm.com.au<svg><use href="#icon-mail"/></svg></li>
    <li>www.brentholmaccountants.com.au<svg><use href="#icon-web"/></svg></li>
  </ul>
</section>

<!-- Business card back -->
<section class="sheet card-back">
  <svg class="sheet-art" viewBox="0 0 400 229" preserveAspectRatio="none" aria-hidden="true">
    <path d="M0 229C100 140 262 82 400 92V229Z" fill="url(#navy-fade)"/>
    <path d="M86 229C166 140 300 94 400 100V229Z" fill="var(--brand-blue)"/>
  </svg>
  <div class="wordmark"><span class="wordmark-square"></span>Brentholm</div>
</section>

</body>
</html>
```